Home Security check flyer

I am a locksmith company. Wanting a flyer designed for postal delivery to houses.
The design is to have a home security check list similar to the one attached (Not exactly the same) targeting locks with some pictures of deadlocks, Deadbolts, Window Locks, Security door locks Etc..
The idea is to get people in there homes to make sure they are secure and if not to call us for a free quote.
Flyer is to catch customers eye so they don't just throw it our. E.G. IS YOUR HOME SECURE on the front
A4 Size to be folded to twice to envelope size.
My company information can be found at
www.brightvalekeyworks.com.au

Reason: Want to try a few changes on some of the eliminated ones.

Target Market(s)

residential homes (Security)

Industry/Entity Type

Locksmith

Requirements
Must have
• My logo and contact information
Based on information from www.brightvalekeyworks.com.au

```html
<!DOCTYPE html>
<html lang="en">
<head>
<meta charset="utf-8">
<title>Home Security Audit Flyer</title>
<link href="https://fonts.googleapis.com/css2?family=Oswald:wght@400;500;600&family=Open+Sans:ital,wght@0,400;0,600;0,700;1,700&display=swap" rel="stylesheet">
<style>
  :root {
    --backdrop: #e4e4e2;
    --paper: #ffffff;
    --ink: #1c1c1c;
    --ink-soft: #3a3a3a;
    --brand-red: #b3151b;
    --badge-blue: #1d6fb8;
    --table-head: #3b3b3d;
    --band-light: #e8e8e9;
    --band-dark: #d6d6d8;
    --panel: #dcdcdd;
    --rule: #2a2a2a;
    --strike: #444444;
  }
  * { box-sizing: border-box; margin: 0; padding: 0; }
  html, body { width: 1200px; height: 956px; overflow: hidden; background: var(--backdrop); }
  body { position: relative; font-family: "Open Sans", Arial, sans-serif; color: var(--ink); }

  .spread {
    position: absolute; left: 20px; top: 62px;
    width: 906px; height: 650px;
    transform: scale(1.2804); transform-origin: 0 0;
    background: var(--paper);
    box-shadow: 0 1px 3px rgba(0,0,0,.18);
  }
  .page { position: absolute; top: 0; height: 650px; }
  .page--left { left: 0; width: 453px; }
  .page--right { left: 453px; width: 453px; }
  .page--right::before {
    content: ""; position: absolute; left: 0; top: 23px; bottom: 0; width: 1px;
    background: linear-gradient(to right, rgba(0,0,0,.08), transparent);
  }

  .header-photo {
    position: absolute; left: 0; top: 0; width: 906px; height: 23px;
    background: linear-gradient(90deg,#3b302a 0%,#8c1218 5%,#b41c22 20%,#c9beb0 21%,#e8e2d8 35%,#f1ede6 55%,#d9d1c4 70%,#4a3a2c 80%,#c8b9a2 86%,#2c2019 100%);
  }

  .audit-title {
    position: absolute; left: 42px; top: 30px; width: 144px; height: 25px;
    background: var(--brand-red); color: #fff;
    font: 500 14px/25px "Oswald", sans-serif; letter-spacing: .2px; text-align: center;
  }
  .lock-badge { position: absolute; left: 190px; top: 30px; width: 22px; height: 22px; }

  .intro { position: absolute; left: 42px; top: 61px; width: 382px; font-size: 7.6px; line-height: 10px; color: var(--ink-soft); }
  .intro p + p { margin-top: 5px; }
  .intro .rate { margin-top: 7px; font-size: 9px; font-weight: 700; font-style: italic; color: var(--ink); }

  .checklist { position: absolute; left: 40px; top: 143px; width: 383px; }
  .checklist__head {
    height: 22px; background: var(--table-head); color: #fff;
    font: 500 9px/22px "Oswald", sans-serif; display: flex; padding-left: 18px;
  }
  .checklist__head span:first-child { width: 148px; }
  .group { padding: 8px 0 0 17px; }
  .group--light { background: linear-gradient(to bottom, #d4d4d6, var(--band-light) 40%); }
  .group--dark { background: var(--band-dark); }
  .group__title { font: 500 7.6px/10px "Oswald", sans-serif; margin-bottom: 2px; }
  .item { display: flex; align-items: center; height: 14.3px; font-size: 6.6px; }
  .item__label { width: 85px; }
  .item__answer { width: 30px; display: flex; align-items: center; gap: 2px; font-size: 6px; }
  .item__answer i { width: 9px; height: 9px; border: .8px solid #444; border-radius: 50%; display: inline-block; background: #fff; }
  .item__note { font-size: 4.6px; line-height: 5.4px; width: 190px; margin-left: 4px; color: var(--ink-soft); }

  .cover-headline {
    position: absolute; left: 41px; top: 30px; width: 372px; height: 25px;
    font: 600 16px/25px "Oswald", sans-serif; color: var(--brand-red); letter-spacing: .3px;
  }

  .product { position: absolute; left: 41px; width: 372px; height: 123px; display: flex; }
  .product__photo { width: 121px; height: 123px; flex: none; }
  .product__panel { position: relative; flex: 1; background: var(--panel); padding: 9px 20px 0 10px; }
  .product__panel::before {
    content: ""; position: absolute; left: -5px; top: 57px;
    border-top: 5px solid transparent; border-bottom: 5px solid transparent; border-right: 5px solid var(--panel);
  }
  .product__name { font: 500 11.5px/14px "Oswald", sans-serif; }
  .product__price { font: 500 19px/23px "Oswald", sans-serif; border-bottom: 1px solid var(--rule); padding-bottom: 2px; }
  .product__rrp { font-size: 8.5px; font-weight: 400; color: var(--strike); text-decoration: line-through; margin-left: 3px; }
  .product__features { margin-top: 5px; font: 500 7.5px/10px "Oswald", sans-serif; }
  .product__copy { font-size: 7.4px; line-height: 9.6px; color: var(--ink-soft); }

  .contact-strip {
    position: absolute; left: 41px; top: 620px; width: 372px; height: 22px;
    background: var(--table-head); color: #fff;
    display: flex; align-items: center; justify-content: space-between; padding: 0 10px;
  }
  .brand { display: flex; align-items: center; gap: 5px; font: 500 9px/1 "Oswald", sans-serif; letter-spacing: .3px; }
  .brand__mark { width: 7px; height: 7px; background: var(--brand-red); }
  .contact-strip__web { font-size: 7px; }
  .contact-strip__cta { font: 500 8px/1 "Oswald", sans-serif; background: var(--brand-red); padding: 3px 6px; }

  .photo-door { background: radial-gradient(circle at 55% 45%, #3a3d42, #111 60%, #050505); }
  .photo-deadlock { background: linear-gradient(90deg,#8a6a45 0%,#6a6a68 12%,#d8d8d6 40%,#efefed 60%,#b9b9b6 100%); }
  .photo-window { background: linear-gradient(160deg,#f2f2ef 0%,#e6e2da 40%,#c9b59a 65%,#a8b06a 100%); }
  .photo-deadbolt { background: linear-gradient(90deg,#5a3418 0%,#7b4a25 50%,#c8a582 80%,#e9e4dc 100%); }
</style>
</head>
<body>
<main class="spread">
  <div class="header-photo" role="img" aria-label="Banner photo of a modern living room interior"></div>

  <section class="page page--left">
    <h1 class="audit-title">HOME SECURITY AUDIT</h1>
    <svg class="lock-badge" viewBox="0 0 22 22" aria-hidden="true">
      <circle cx="11" cy="11" r="10.5" fill="var(--badge-blue)"/>
      <circle cx="11" cy="11" r="8.5" fill="none" stroke="#fff" stroke-width=".8"/>
      <path d="M8 10V8.3a3 3 0 0 1 6 0V10" fill="none" stroke="#fff" stroke-width="1.4"/>
      <rect x="6.8" y="10" width="8.4" height="6" rx="1" fill="#fff"/>
    </svg>

    <div class="intro">
      <p>House-breaking is one of the most common crimes and can occur at any time of the day or night. This checklist is designed to help you take a fresh look at your home security.</p>
      <p>You can take steps to reduce identified risk areas in your home and reduce the likelihood of becoming a victim of crime or a repeat victim of crime.</p>
      <p class="rate">How does your home security rate?</p>
    </div>

    <div class="checklist">
      <div class="checklist__head"><span>PRESENT CONDITION</span><span>CONSIDER MAKING CHANGES TO THE ITEM TICKED NO</span></div>

      <div class="group group--light" style="height:68px">
        <h2 class="group__title">SECURITY DOORS</h2>
        <div class="item"><span class="item__label">At all entry/exits?</span><span class="item__answer">Y <i></i></span><span class="item__answer">N <i></i></span><span class="item__note">Security doors deter intruders from entering your home</span></div>
        <div class="item"><span class="item__label">Finger guards?</span><span class="item__answer">Y <i></i></span><span class="item__answer">N <i></i></span><span class="item__note">Finger guards prevent the lock on your security door/s being tampered with</span></div>
        <div class="item"><span class="item__label">Triple locks?</span><span class="item__answer">Y <i></i></span><span class="item__answer">N <i></i></span><span class="item__note">Triple locks increase the strength and security of your doors</span></div>
      </div>

      <div class="group group--light" style="height:98px">
        <h2 class="group__title">MAIN ENTRY/EXIT DOORS</h2>
        <div class="item"><span class="item__label">Front - solid core?</span><span class="item__answer">Y <i></i></span><span class="item__answer">N <i></i></span><span class="item__note">Solid doors are preferred; the door should be as strong as the lock</span></div>
        <div class="item"><span class="item__label">Front - viewer?</span><span class="item__answer">Y <i></i></span><span class="item__answer">N <i></i></span><span class="item__note">Door viewers help you see who is outside your front door before you open it</span></div>
        <div class="item"><span class="item__label">Back - solid core?</span><span class="item__answer">Y <i></i></span><span class="item__answer">N <i></i></span><span class="item__note">Solid doors are preferred; hollow core doors should be avoided</span></div>
        <div class="item"><span class="item__label">Adequate locks?</span><span class="item__answer">Y <i></i></span><span class="item__answer">N <i></i></span><span class="item__note">Dead locks are the best type of lock to use on entry/exit doors</span></div>
        <div class="item"><span class="item__label">Keyed alike?</span><span class="item__answer">Y <i></i></span><span class="item__answer">N <i></i></span><span class="item__note">For safety and ease of use, one key opens all doors</span></div>
      </div>

      <div class="group group--dark" style="height:35px">
        <h2 class="group__title">SLIDING DOORS</h2>
        <div class="item"><span class="item__label">Patio bolts?</span><span class="item__answer">Y <i></i></span><span class="item__answer">N <i></i></span><span class="item__note">Keyed patio bolts on sliding doors strengthen the security of these doors</span></div>
      </div>

      <div class="group group--light" style="height:79px">
        <h2 class="group__title">WINDOWS</h2>
        <div class="item"><span class="item__label">Key operated locks?</span><span class="item__answer">Y <i></i></span><span class="item__answer">N <i></i></span><span class="item__note">Key operated locks strengthen the security of your windows</span></div>
        <div class="item"><span class="item__label">Keyed alike?</span><span class="item__answer">Y <i></i></span><span class="item__answer">N <i></i></span><span class="item__note">For safety and ease of use, one key opens all windows</span></div>
        <div class="item"><span class="item__label">Security screens?</span><span class="item__answer">Y <i></i></span><span class="item__answer">N <i></i></span><span class="item__note">Security screens, grilles and shutters allow ventilation and can provide security</span></div>
        <div class="item"><span class="item__label">Warning stickers?</span><span class="item__answer">Y <i></i></span><span class="item__answer">N <i></i></span><span class="item__note">Warning stickers may deter intruders from stealing your property</span></div>
      </div>

      <div class="group group--dark" style="height:83px">
        <h2 class="group__title">LIGHTING</h2>
        <div class="item"><span class="item__label">Main entry/exits?</span><span class="item__answer">Y <i></i></span><span class="item__answer">N <i></i></span><span class="item__note">The main entry/exit areas to your home should be well lit</span></div>
        <div class="item"><span class="item__label">Timers fitted?</span><span class="item__answer">Y <i></i></span><span class="item__answer">N <i></i></span><span class="item__note">Lights left on inside your home when you are out often deter intruders</span></div>
        <div class="item"><span class="item__label">Timers used?</span><span class="item__answer">Y <i></i></span><span class="item__answer">N <i></i></span><span class="item__note">Timers should be activated when away from your home at night</span></div>
        <div class="item"><span class="item__label">Sensor lighting?</span><span class="item__answer">Y <i></i></span><span class="item__answer">N <i></i></span><span class="item__note">Sensor lighting in 'high risk' areas deter intruders from entering your home</span></div>
      </div>

      <div class="group group--light" style="height:88px">
        <h2 class="group__title">PROPERTY MARKING</h2>
        <div class="item"><span class="item__label">Engraved with code?</span><span class="item__answer">Y <i></i></span><span class="item__answer">N <i></i></span><span class="item__note">Property engraving and using WARNING stickers on your property reduces the risk of it being stolen</span></div>
        <div class="item"><span class="item__label">Code recorded?</span><span class="item__answer">Y <i></i></span><span class="item__answer">N <i></i></span><span class="item__note">Your Property ID code should be recorded with police to assist them to contact owners of recovered items</span></div>
        <div class="item"><span class="item__label">Inventory list?</span><span class="item__answer">Y <i></i></span><span class="item__answer">N <i></i></span><span class="item__note">Recording serial numbers, makes, models and descriptions of your property helps police recover stolen items and will assist you to make an insurance claim (you may wish to photograph items and store somewhere safe)</span></div>
      </div>
    </div>
  </section>

  <section class="page page--right">
    <h2 class="cover-headline">IS YOUR HOME SECURE?</h2>

    <article class="product" style="top:61px">
      <div class="product__photo photo-door" role="img" aria-label="Photo of a black digital keypad security door lock"></div>
      <div class="product__panel">
        <h3 class="product__name">SECURITY DOOR LOCKS</h3>
        <p class="product__price">$69.99<span class="product__rrp">RRP 89.99</span></p>
        <p class="product__features">FEATURES</p>
        <p class="product__copy">Lorem ipsum dolor sit amet, consectetur adipisicing elit, sed do eiusmod tempor incididunt ut labore et dolore magna aliqua. Ut enim ad minim veniam, quis nostrud exercitation ullamco.</p>
      </div>
    </article>

    <article class="product" style="top:203px">
      <div class="product__photo photo-deadlock" role="img" aria-label="Photo of a hand holding a mortice deadlock beside a door edge"></div>
      <div class="product__panel">
        <h3 class="product__name">DEADLOCKS</h3>
        <p class="product__price">$29.99<span class="product__rrp">RRP49.00</span></p>
        <p class="product__features">FEATURES</p>
        <p class="product__copy">Lorem ipsum dolor sit amet, consectetur adipisicing elit, sed do eiusmod tempor incididunt ut labore et dolore magna aliqua. Ut enim ad minim veniam, quis nostrud exercitation ullamco.</p>
      </div>
    </article>

    <article class="product" style="top:346px">
      <div class="product__photo photo-window" role="img" aria-label="Photo of a hand operating a window lock"></div>
      <div class="product__panel">
        <h3 class="product__name">WINDOW LOCKS</h3>
        <p class="product__price">$49.99<span class="product__rrp">RRP69.99</span></p>
        <p class="product__features">FEATURES</p>
        <p class="product__copy">Lorem ipsum dolor sit amet, consectetur adipisicing elit, sed do eiusmod tempor incididunt ut labore et dolore magna aliqua. Ut enim ad minim veniam, quis nostrud exercitation ullamco.</p>
      </div>
    </article>

    <article class="product" style="top:491px">
      <div class="product__photo photo-deadbolt" role="img" aria-label="Photo of a deadbolt on a timber door being turned by hand"></div>
      <div class="product__panel">
        <h3 class="product__name">DEADBOLTS</h3>
        <p class="product__price">$39.99<span class="product__rrp">RRP59.99</span></p>
        <p class="product__features">FEATURES</p>
        <p class="product__copy">Lorem ipsum dolor sit amet, consectetur adipisicing elit, sed do eiusmod tempor incididunt ut labore et dolore magna aliqua. Ut enim ad minim veniam, quis nostrud exercitation ullamco.</p>
      </div>
    </article>

    <footer class="contact-strip">
      <span class="brand"><span class="brand__mark"></span>BRIGHTVALE KEYWORKS</span>
      <span class="contact-strip__web">www.brightvalekeyworks.com.au</span>
      <span class="contact-strip__cta">CALL US FOR A FREE QUOTE</span>
    </footer>
  </section>
</main>
</body>
</html>
```